Tavo Payments Business card refresh

Need a new design of our business card The info is not what is on these cards i sent this for a reference. I can email all the info over
Info would be Derek Whitfield Chief TAVO is the title. our new address is 47615 Birch Hollow Rd. Cedar Ridge Ca 91384 Cell number is 805-634-2917 Work number is 855-482-7309 ext 347 Derek@tavopayments.com is my email address
Target Market(s)
Merchant Services all businesses that take credit cards
Industry/Entity Type
Merchant Services / Credit Card processing
Contact Information for Business Card
Need a new design of our business card The info is not what is on these cards i sent this for a reference. I can email all the info over Info would be Derek Whitfield Chief TAVO is the title. our new address is 47615 Birch Hollow Rd. Cedar Ridge Ca 91384 Cell number is 805-634-2917 Work number is 855-482-7309 ext 347 Derek@tavopayments.com is my email address
Requirements
Must have
- My logo and colors from my brand guidelines
Nice to have
- i sent some designs just need a new refresh
Should not have
- nothing specific

```html
<!DOCTYPE html>
<html lang="en">
<head>
<meta charset="utf-8">
<title>Tavo Payments – Business Card</title>
<link rel="stylesheet" href="https://fonts.googleapis.com/css2?family=Montserrat:wght@700&family=Questrial&display=swap">
<style>
  :root {
    --backdrop: #342a29;
    --card: #f2ffe9;
    --brand-green: #5aff00;
    --band-green: #b8ff80;
    --ink: #342a29;
  }
  html, body {
    margin: 0;
    padding: 0;
    width: 1200px;
    height: 1200px;
    overflow: hidden;
    background: var(--backdrop);
  }
  .business-card {
    display: block;
    width: 1200px;
    height: 1200px;
  }
  .card-face { fill: var(--card); }
  .accent-shape { fill: var(--brand-green); }
  .header-band { fill: var(--band-green); }
  .holder-name {
    font-family: "Montserrat", sans-serif;
    font-weight: 700;
    font-size: 47px;
    fill: var(--ink);
    letter-spacing: -0.5px;
  }
  .holder-title,
  .contact-line,
  .contact-label,
  .contact-extension,
  .contact-email,
  .contact-address {
    font-family: "Questrial", sans-serif;
    fill: var(--ink);
  }
  .holder-title { font-size: 31px; }
  .contact-label { font-size: 30px; }
  .contact-colon { font-size: 12px; }
  .contact-line { font-size: 34px; letter-spacing: 1px; }
  .contact-extension { font-size: 24px; }
  .contact-email { font-size: 39px; }
  .contact-address { font-size: 29px; }
</style>
</head>
<body>
<svg class="business-card" viewBox="0 0 1200 1200" xmlns="http://www.w3.org/2000/svg" aria-label="Derek Whitfield business card, Tavo Payments">
  <rect class="card-face" x="150" y="328" width="911" height="551"/>
  <polygon class="accent-shape accent-corner" points="887,436 1061,328 1061,436"/>
  <rect class="header-band" x="150" y="436" width="911" height="6"/>
  <polygon class="accent-shape accent-wedge" points="150,442 878,442 146,879"/>

  <text class="holder-name" x="598" y="395" text-anchor="middle">Derek Whitfield</text>
  <text class="holder-title" x="598" y="426" text-anchor="middle">Chief TAVO</text>

  <text class="contact-label" x="732" y="671">c</text>
  <text class="contact-label contact-colon" x="760" y="667">:</text>
  <text class="contact-line" x="1012" y="672" text-anchor="end">805-634-2917</text>

  <text class="contact-label" x="728" y="710">o</text>
  <text class="contact-label contact-colon" x="760" y="706">:</text>
  <text class="contact-line" x="1012" y="711" text-anchor="end">855-482-7309</text>

  <text class="contact-extension" x="1012" y="747" text-anchor="end">ext 347</text>
  <text class="contact-email" x="1012" y="789" text-anchor="end">Derek@tavopayments.com</text>
  <text class="contact-address" x="1012" y="836" text-anchor="end">47615 Birch Hollow Rd. Cedar Ridge Ca 91384</text>
</svg>
</body>
</html>
```